The Timber Loft

We need a business card design for our wardrobe company.
Please visit our website www.zorvelcabinets.com to get an idea of who we are.

```html
<!DOCTYPE html>
<html lang="en">
<head>
<meta charset="utf-8">
<title>The Timber Loft — Business Card</title>
<link rel="stylesheet" href="https://fonts.googleapis.com/css2?family=Lato:wght@400;700;900&display=swap">
<style>
  :root {
    --page-bg: #151515;
    --card-bg: #2c2a2b;
    --card-edge: #3a3839;
    --text-main: #e6e6e6;
    --text-soft: #b9b9b9;
    --rule: #9a9a9a;
    --emboss-text: #7a787a;
  }
  * { margin: 0; padding: 0; box-sizing: border-box; }
  html, body {
    width: 1200px;
    height: 900px;
    overflow: hidden;
    background: var(--page-bg);
    font-family: "Lato", sans-serif;
  }
  .sheet {
    width: 1200px;
    height: 900px;
    display: flex;
    flex-direction: column;
    align-items: center;
    justify-content: center;
    gap: 48px;
  }
  .card {
    width: 700px;
    height: 400px;
    background: var(--card-bg);
    border: 1px solid var(--card-edge);
    position: relative;
  }
  .card--front {
    display: flex;
    align-items: center;
    padding: 0 56px;
  }
  .brand {
    width: 290px;
  }
  .brand__row {
    display: flex;
    align-items: center;
    gap: 12px;
  }
  .brand__mark {
    width: 16px;
    height: 16px;
    border: 2px solid var(--text-soft);
  }
  .brand__name {
    font-weight: 700;
    font-size: 19px;
    letter-spacing: 1.5px;
    text-transform: uppercase;
    color: var(--text-soft);
  }
  .brand__tagline {
    margin-top: 8px;
    margin-left: 30px;
    font-size: 15px;
    color: var(--text-soft);
  }
  .divider {
    width: 1px;
    height: 170px;
    background: var(--rule);
    margin: 0 34px 0 10px;
  }
  .contact {
    color: var(--text-main);
  }
  .contact__name {
    font-weight: 900;
    font-size: 24px;
  }
  .contact__role {
    font-size: 17px;
    margin-bottom: 14px;
  }
  .contact__address {
    font-size: 17px;
    line-height: 1.3;
    margin-bottom: 8px;
  }
  .contact__list {
    list-style: none;
    font-size: 17px;
    line-height: 1.35;
  }
  .contact__list li {
    display: flex;
    align-items: center;
    gap: 10px;
  }
  .contact__list svg {
    width: 14px;
    height: 14px;
    flex: none;
  }
  .card--back {
    display: flex;
    flex-direction: column;
    align-items: center;
    justify-content: center;
    gap: 60px;
  }
  .back__name {
    display: flex;
    align-items: center;
    gap: 22px;
  }
  .back__mark {
    width: 40px;
    height: 40px;
    border: 4px solid var(--emboss-text);
  }
  .back__title {
    font-weight: 700;
    font-size: 48px;
    letter-spacing: 3px;
    text-transform: uppercase;
    color: var(--emboss-text);
  }
  .back__url {
    font-size: 20px;
    color: var(--text-main);
  }
  .back__url strong { font-weight: 900; }
</style>
</head>
<body>
<main class="sheet">
  <section class="card card--front" aria-label="Business card front">
    <div class="brand">
      <div class="brand__row">
        <span class="brand__mark" aria-hidden="true"></span>
        <span class="brand__name">The Timber Loft</span>
      </div>
      <p class="brand__tagline">Built Square and True</p>
    </div>
    <div class="divider" aria-hidden="true"></div>
    <div class="contact">
      <p class="contact__name">Marcus Hale</p>
      <p class="contact__role">Managing Director</p>
      <p class="contact__address">Arden Court, 42 Mill Lane<br>London N4 3QT</p>
      <ul class="contact__list">
        <li>
          <svg viewBox="0 0 16 16" aria-hidden="true"><path fill="#e6e6e6" d="M3.6 1.5l2.2 2.6-1.2 1.6c.9 2 2.4 3.5 4.4 4.4l1.6-1.2 2.6 2.2-1.4 2.4C6.6 13.2 2.8 9.4 1.2 3.2z"/></svg>
          0207 555 0148
        </li>
        <li>
          <svg viewBox="0 0 16 16" aria-hidden="true"><rect x="1.5" y="3.5" width="13" height="9" fill="none" stroke="#e6e6e6" stroke-width="1.4"/><path d="M1.5 3.5l6.5 5 6.5-5" fill="none" stroke="#e6e6e6" stroke-width="1.4"/></svg>
          info@zorvelcabinets.com
        </li>
        <li>
          <svg viewBox="0 0 16 16" aria-hidden="true"><circle cx="8" cy="8" r="6.5" fill="none" stroke="#e6e6e6" stroke-width="1.4"/><ellipse cx="8" cy="8" rx="2.8" ry="6.5" fill="none" stroke="#e6e6e6" stroke-width="1.2"/><path d="M1.5 8h13" stroke="#e6e6e6" stroke-width="1.2"/></svg>
          www.zorvelcabinets.com
        </li>
      </ul>
    </div>
  </section>

  <section class="card card--back" aria-label="Business card back">
    <div class="back__name">
      <span class="back__mark" aria-hidden="true"></span>
      <span class="back__title">The Timber Loft</span>
    </div>
    <p class="back__url">www.<strong>zorvelcabinets</strong>.com</p>
  </section>
</main>
</body>
</html>
```